Letterhead, business card and email signature design

I have a new company and I would like a professional letterhead, business card and email signature designed. Id like the business card to have room for a photo of the bearer. I'd also like the template to be editable so we can adapt for future members of staff etc.

```html
<!DOCTYPE html>
<html lang="en">
<head>
<meta charset="UTF-8">
<title>Verrin Networks — Stationery Set</title>
<link href="https://fonts.googleapis.com/css2?family=Open+Sans:wght@400;600&display=swap" rel="stylesheet">
<style>
  :root{
    --navy:#1e3560;
    --magenta:#9e1f5e;
    --plum:#5b2e6b;
    --wine-light:#8c1b50;
    --wine-dark:#4a0524;
    --ink:#2a2a33;
    --muted:#6b6b78;
    --paper:#ffffff;
    --bg:#e4e4e7;
    --rule:#e7b9cf;
    --band:linear-gradient(90deg,var(--navy) 0%,var(--plum) 45%,var(--magenta) 100%);
  }
  *{box-sizing:border-box;margin:0;padding:0}
  html,body{width:1200px;height:1200px;overflow:hidden}
  body{background:var(--bg);font-family:"Open Sans",Arial,sans-serif;color:var(--ink);position:relative}
  .icon{width:11px;height:11px;fill:currentColor;flex:none}

  /* brand lockup */
  .brand{display:flex;align-items:center;gap:10px}
  .brand-dot{border-radius:50%;background:var(--navy);flex:none}
  .brand-name{font-weight:600;color:var(--navy);letter-spacing:.06em;white-space:nowrap}

  /* shared */
  .sheet{position:absolute;background:var(--paper);box-shadow:0 6px 18px rgba(0,0,0,.14)}
  .photo{background:linear-gradient(160deg,#dfe4ec,#b9c6da);border:3px solid #fff;outline:1px solid #9a9aa6}
  .band{background:var(--band);color:#fff;display:flex;align-items:center}
  .band-disc{position:absolute;border-radius:50%;background:var(--paper);border:3px solid var(--magenta)}
  .contact{list-style:none;font-size:10px;color:var(--muted)}
  .contact li{display:flex;align-items:center;gap:6px;margin-bottom:3px}
  .contact .icon{color:var(--magenta)}

  /* business card front */
  .card-front{left:90px;top:150px;width:380px;height:217px;overflow:hidden}
  .card-front .brand{position:absolute;right:22px;top:22px}
  .card-front .brand-dot{width:30px;height:30px}
  .card-front .brand-name{font-size:15px}
  .card-front .photo{position:absolute;left:22px;top:78px;width:62px;height:76px}
  .card-front .identity{position:absolute;left:98px;top:84px}
  .name{font-weight:600;color:var(--navy);letter-spacing:.04em}
  .card-front .name{font-size:16px}
  .role{font-size:9px;color:var(--muted)}
  .card-front .contact{position:absolute;left:22px;top:160px;font-size:8.5px}
  .card-front .contact li{margin-bottom:1px}
  .card-front .band{position:absolute;left:0;right:0;bottom:0;height:20px;padding-left:22px;font-size:8.5px;gap:6px}
  .card-front .band .icon{width:9px;height:9px}
  .card-front .band-disc{right:24px;bottom:6px;width:28px;height:28px}

  /* business card back */
  .card-back{left:90px;top:420px;width:380px;height:217px;
    background:radial-gradient(circle at 50% 40%,var(--wine-light),var(--wine-dark));
    display:flex;align-items:center;justify-content:center}
  .card-back .brand-dot{width:48px;height:48px;background:#fff}
  .card-back .brand-name{font-size:22px;color:#fff}

  /* letterhead */
  .letterhead{left:530px;top:40px;width:580px;height:820px}
  .letterhead .brand{position:absolute;left:0;right:0;top:54px;justify-content:center}
  .letterhead .brand-dot{width:46px;height:46px}
  .letterhead .brand-name{font-size:22px}
  .letter-body{position:absolute;left:56px;right:56px;top:170px;font-size:11.5px;line-height:1.75;color:#3a3a44}
  .letter-body p{margin-bottom:18px}
  .closing{margin-top:26px}
  .signature{width:150px;height:46px;margin:8px 0 4px;background:linear-gradient(90deg,rgba(30,53,96,.10),rgba(30,53,96,.02));border-radius:4px}
  .signer{font-weight:600;color:var(--navy)}
  .letter-foot{position:absolute;left:0;right:0;bottom:30px}
  .letter-foot .rule{height:1px;background:var(--rule);margin:0 0 6px}
  .letter-foot .band{height:70px;padding:0 90px 0 34px;gap:28px;font-size:10.5px}
  .letter-foot .contact{color:#fff;font-size:10.5px}
  .letter-foot .contact .icon{color:#fff}
  .letter-foot .divider{width:1px;height:40px;background:rgba(255,255,255,.5)}
  .letter-foot .rule.bottom{margin:6px 0 0}
  .letter-foot .band-disc{right:22px;top:-4px;width:70px;height:70px}

  /* email signature */
  .email-sig{left:150px;top:905px;width:900px;height:250px;overflow:hidden}
  .email-sig .brand{position:absolute;right:34px;top:26px}
  .email-sig .brand-dot{width:40px;height:40px}
  .email-sig .brand-name{font-size:19px}
  .email-sig .photo{position:absolute;left:34px;top:40px;width:118px;height:146px}
  .email-sig .details{position:absolute;left:176px;top:44px;padding-left:18px;border-left:1px solid var(--magenta);height:130px}
  .email-sig .name{font-size:20px;color:var(--magenta)}
  .email-sig .role{margin-bottom:10px}
  .email-sig .band{position:absolute;left:0;right:0;bottom:0;height:30px;padding:0 0 0 34px;font-size:12px;letter-spacing:.03em}
  .social{position:absolute;right:90px;bottom:4px;display:flex;gap:10px;list-style:none}
  .social li{width:22px;height:22px;border-radius:50%;border:2px solid #fff;background:var(--magenta)}
  .email-sig .band-disc{right:24px;bottom:2px;width:36px;height:36px}
</style>
</head>
<body>
<svg width="0" height="0" style="position:absolute" aria-hidden="true">
  <symbol id="i-phone" viewBox="0 0 18 18"><path d="M3 1h4l1.3 4.5-2.2 1.2a11 11 0 0 0 5.2 5.2l1.2-2.2L17 11v4a2 2 0 0 1-2 2A15 15 0 0 1 1 3a2 2 0 0 1 2-2z"/></symbol>
  <symbol id="i-mail" viewBox="0 0 18 18"><path d="M1 4h16v10H1zM2 5l7 5 7-5v-.5H2z" fill-rule="evenodd"/></symbol>
  <symbol id="i-pin" viewBox="0 0 18 18"><path d="M9 1a6 6 0 0 0-6 6c0 5 6 10 6 10s6-5 6-10a6 6 0 0 0-6-6zm0 8.5a2.5 2.5 0 1 1 0-5 2.5 2.5 0 0 1 0 5z"/></symbol>
  <symbol id="i-web" viewBox="0 0 18 18"><path d="M9 1a8 8 0 1 0 0 16A8 8 0 0 0 9 1zm0 1.6c.9 1 1.6 2.7 1.8 5.6H7.2C7.4 5.3 8.1 3.6 9 2.6zM2.7 8.2a6.4 6.4 0 0 1 3.5-5c-.5 1.3-.9 3-.9 5zm0 1.6h2.6c.1 2 .4 3.7.9 5a6.4 6.4 0 0 1-3.5-5zm4.5 0h3.6c-.2 2.9-.9 4.6-1.8 5.6-.9-1-1.6-2.7-1.8-5.6zm5.5 0h2.6a6.4 6.4 0 0 1-3.5 5c.5-1.3.8-3 .9-5zm0-1.6c-.1-2-.4-3.7-.9-5a6.4 6.4 0 0 1 3.5 5z"/></symbol>
</svg>

<!-- Business card — front -->
<section class="sheet card-front" aria-label="Business card front">
  <div class="brand"><span class="brand-dot"></span><span class="brand-name">VERRIN NETWORKS</span></div>
  <div class="photo" role="img" aria-label="Portrait photo of the card holder"></div>
  <div class="identity">
    <h2 class="name">MARA ELLISON</h2>
    <p class="role">Director</p>
  </div>
  <ul class="contact">
    <li><svg class="icon"><use href="#i-phone"/></svg>1-555-010200</li>
    <li><svg class="icon"><use href="#i-mail"/></svg>mara@verrinnetworks.com</li>
    <li><svg class="icon"><use href="#i-web"/></svg>www.verrinnetworks.com</li>
  </ul>
  <div class="band"><svg class="icon"><use href="#i-pin"/></svg>Dummy city, Dummy Country Dummy Land</div>
  <span class="band-disc"></span>
</section>

<!-- Business card — back -->
<section class="sheet card-back" aria-label="Business card back">
  <div class="brand"><span class="brand-dot"></span><span class="brand-name">VERRIN NETWORKS</span></div>
</section>

<!-- Letterhead -->
<section class="sheet letterhead" aria-label="Letterhead">
  <div class="brand"><span class="brand-dot"></span><span class="brand-name">VERRIN NETWORKS</span></div>
  <div class="letter-body">
    <p>Lorem ipsum dolor sit amet, consectetur adipiscing elit. Sed at ante. Mauris eleifend, quam a vulputate dictum, massa quam dapibus leo, eget vulputate orci purus ut lorem. In fringilla mi in ligula. Pellentesque aliquam quam vel dolor. Nunc adipiscing. Sed quamodio, tempus ac, aliquam molestie varius ac, tellus. Vestibulum ut nulla aliquam risus rutrum interdum. Pellentesque lorem.</p>
    <p>Curabitur sit amet erat quis risus feugiat viverra. Pellentesque augue justo, sagittis et, lacinia at, venenatis non, arcu. Nunc nec libero. In cursus dictum risus. Etiam tristique nisl a nulla. Ut a orci. Curabitur dolor nunc, egestas at, accumsan at, malesuada nec, magna. Nulla facilisi. Nunc volutpat. Vestibulum ante ipsum primis in faucibus orci luctus et ultrices posuere cubilia Curae; Ut sit amet orci vel mauris blandit vehicula. Nullam quis enim. Integer dignissim viverra velit. Curabitur in odio.</p>
    <p class="closing">Thanking you,</p>
    <div class="signature" role="img" aria-label="Handwritten signature"></div>
    <p class="signer">Mara Ellison</p>
  </div>
  <footer class="letter-foot">
    <div class="rule"></div>
    <div class="band">
      <ul class="contact">
        <li><svg class="icon"><use href="#i-phone"/></svg>1-555-010200</li>
        <li><svg class="icon"><use href="#i-mail"/></svg>mara@verrinnetworks.com</li>
        <li><svg class="icon"><use href="#i-web"/></svg>www.verrinnetworks.com</li>
      </ul>
      <span class="divider"></span>
      <ul class="contact">
        <li><svg class="icon"><use href="#i-pin"/></svg>Dummy city</li>
        <li style="padding-left:17px">Dummy Country Land</li>
      </ul>
    </div>
    <div class="rule bottom"></div>
    <span class="band-disc"></span>
  </footer>
</section>

<!-- Email signature -->
<section class="sheet email-sig" aria-label="Email signature">
  <div class="brand"><span class="brand-dot"></span><span class="brand-name">VERRIN NETWORKS</span></div>
  <div class="photo" role="img" aria-label="Portrait photo of the sender"></div>
  <div class="details">
    <h2 class="name">MARA ELLISON</h2>
    <p class="role">Director</p>
    <ul class="contact">
      <li><svg class="icon"><use href="#i-phone"/></svg>1-555-010200</li>
      <li><svg class="icon"><use href="#i-mail"/></svg>mara@verrinnetworks.com</li>
      <li><svg class="icon"><use href="#i-pin"/></svg>Dummy city, Dummy Country Dummy Land</li>
    </ul>
  </div>
  <div class="band">www.verrinnetworks.com</div>
  <ul class="social" aria-label="Social profiles">
    <li></li><li></li><li></li><li></li>
  </ul>
  <span class="band-disc"></span>
</section>
</body>
</html>
```